Business Card Design

I need a business card design for my law office based in Pasadena, California. I am a sole practitioner and I specialize in business transaction and litigation, probate and estate planning, taxation law, corporate and business formation, immigration and real estate. I want something that is simple, yet stands out.

A friend helped to create a logo about 6 years ago. I am open to new ideas to changing the logo.

Industry/Entity Type

Business

Contact Information for Business Card

Law Offices of Dorvan L. Mabry
842 W. Larkspur Ave., Suite 319
Pasadena, CA 90287
Tel: 626-555-0174
Fax: 626-555-0139
Email: dmabry@dlmlegalgroup.example

Attorney: Dorvan L. Mabry

```html
<!DOCTYPE html>
<html lang="en">
<head>
<meta charset="utf-8">
<title>Law Offices of Dorvan L. Mabry – Business Card</title>
<link rel="stylesheet" href="https://fonts.googleapis.com/css2?family=Arimo:wght@400&family=Tinos:wght@400&display=swap">
<style>
  :root {
    --backdrop: #e9e7e3;
    --card: #fbfbfb;
    --card-edge: #e2e2e2;
    --ink: #1c1c1c;
    --mark: #2b2626;
    --rule: #3a3a3a;
    --soft-rule: #9a9a9a;
  }
  * { margin: 0; padding: 0; box-sizing: border-box; }
  html, body { width: 1200px; height: 892px; overflow: hidden; }
  body {
    background: var(--backdrop);
    display: flex;
    align-items: center;
    justify-content: center;
    gap: 40px;
    color: var(--ink);
  }
  .card {
    position: relative;
    width: 540px;
    height: 309px;
    background: linear-gradient(160deg, #ffffff 0%, var(--card) 55%, #f0f0f0 100%);
    border: 1px solid var(--card-edge);
    border-radius: 18px;
    box-shadow: 0 10px 30px rgba(0,0,0,0.12);
    overflow: hidden;
  }

  /* Front */
  .brand {
    position: absolute;
    left: 34px;
    top: 40px;
    display: flex;
    align-items: center;
    gap: 16px;
  }
  .brand-square {
    width: 46px;
    height: 46px;
    background: var(--mark);
  }
  .brand-name {
    font-family: "Tinos", serif;
    font-weight: 400;
    color: var(--ink);
    line-height: 1.1;
  }
  .brand-name .small { display: block; font-size: 11px; letter-spacing: 4px; text-transform: uppercase; }
  .brand-name .large { display: block; font-size: 27px; letter-spacing: 1px; text-transform: uppercase; }

  .divider-h {
    position: absolute;
    left: 34px;
    right: 190px;
    top: 146px;
    height: 1px;
    background: var(--rule);
  }
  .divider-v {
    position: absolute;
    left: 34px;
    top: 146px;
    width: 1px;
    height: 140px;
    background: var(--rule);
  }
  .attorney {
    position: absolute;
    right: 30px;
    top: 122px;
    text-align: right;
    font-family: "Tinos", serif;
  }
  .attorney .name { font-size: 25px; line-height: 1; }
  .attorney .title { font-size: 15px; margin-top: 4px; }

  .contacts {
    position: absolute;
    left: 50px;
    top: 170px;
    list-style: none;
    font-family: "Arimo", sans-serif;
    font-size: 14px;
  }
  .contacts li {
    display: flex;
    align-items: center;
    gap: 12px;
    height: 23px;
  }
  .contacts svg { width: 13px; height: 13px; flex: none; }

  /* Back */
  .back-mark {
    position: absolute;
    left: 300px;
    top: 40px;
    width: 160px;
    height: 160px;
    border: 2px solid var(--mark);
    padding: 8px;
  }
  .back-mark div { width: 100%; height: 100%; background: var(--mark); }
  .back-name {
    position: absolute;
    left: 40px;
    bottom: 48px;
    font-family: "Tinos", serif;
    font-weight: 400;
    color: var(--ink);
    line-height: 1.1;
  }
  .back-name .small { display: block; font-size: 13px; letter-spacing: 7px; text-transform: uppercase; }
  .back-name .large { display: block; font-size: 38px; letter-spacing: 1px; text-transform: uppercase; }
</style>
</head>
<body>

  <section class="card card-front">
    <div class="brand">
      <div class="brand-square"></div>
      <div class="brand-name">
        <span class="small">Law Offices of</span>
        <span class="large">Dorvan L. Mabry</span>
      </div>
    </div>

    <div class="divider-h"></div>
    <div class="divider-v"></div>

    <div class="attorney">
      <div class="name">Dorvan L. Mabry</div>
      <div class="title">Attorney</div>
    </div>

    <ul class="contacts">
      <li>
        <svg viewBox="0 0 13 13" aria-hidden="true"><rect width="13" height="13" rx="2" fill="#1c1c1c"/><path d="M4 3.2c.4-.3.8 0 1 .4l.5 1c.2.4 0 .7-.3.9-.2.2-.2.4 0 .8.4.7.8 1.1 1.5 1.5.4.2.6.2.8 0 .2-.3.5-.5.9-.3l1 .5c.4.2.7.6.4 1-.5.8-1.3 1.1-2.3.6C5.9 8.7 4.3 7.1 3.5 5.5 3 4.5 3.3 3.7 4 3.2z" fill="#fff"/></svg>
        626-555-0174
      </li>
      <li>
        <svg viewBox="0 0 13 13" aria-hidden="true"><rect width="13" height="13" rx="2" fill="#1c1c1c"/><rect x="3.5" y="2.5" width="6" height="3" fill="#fff"/><rect x="2.5" y="5.5" width="8" height="4" fill="#fff"/><rect x="4" y="8" width="5" height="2.5" fill="#1c1c1c"/></svg>
        626-555-0139
      </li>
      <li>
        <svg viewBox="0 0 13 13" aria-hidden="true"><rect width="13" height="13" rx="2" fill="#1c1c1c"/><circle cx="6.5" cy="6.5" r="3.6" fill="none" stroke="#fff" stroke-width="1"/><path d="M2.9 6.5h7.2M6.5 2.9c-1.6 2-1.6 5.2 0 7.2M6.5 2.9c1.6 2 1.6 5.2 0 7.2" fill="none" stroke="#fff" stroke-width=".8"/></svg>
        www.dlmlegalgroup.example
      </li>
      <li>
        <svg viewBox="0 0 13 13" aria-hidden="true"><rect width="13" height="13" rx="2" fill="#1c1c1c"/><rect x="2.5" y="3.8" width="8" height="5.4" fill="none" stroke="#fff" stroke-width="1"/><path d="M2.5 3.8l4 3 4-3" fill="none" stroke="#fff" stroke-width="1"/></svg>
        dmabry@dlmlegalgroup.example
      </li>
      <li>
        <svg viewBox="0 0 13 13" aria-hidden="true"><rect width="13" height="13" rx="2" fill="#1c1c1c"/><path d="M6.5 2.3a2.9 2.9 0 0 1 2.9 2.9c0 2.1-2.9 5.5-2.9 5.5S3.6 7.3 3.6 5.2a2.9 2.9 0 0 1 2.9-2.9z" fill="#fff"/><circle cx="6.5" cy="5.2" r="1.1" fill="#1c1c1c"/></svg>
        842 W. Larkspur Ave., Suite 319 Pasadena, CA 90287
      </li>
    </ul>
  </section>

  <section class="card card-back">
    <div class="back-mark"><div></div></div>
    <div class="back-name">
      <span class="small">Law Offices of</span>
      <span class="large">Dorvan L. Mabry</span>
    </div>
  </section>

</body>
</html>
```